Kitchen Tools Infographic - Helpful Items for Healthy Home Meals

We are a weight loss company that provides holistic, natural nutrition programs to consumers -- you can see our web site at www.FernQuill.com. We need a simple infographic to be shared on social media and via email. The topic for the infographic is "Equip Your Kitchen for Healthy Home Meals". We've outlined 5 groups of kitchen tools that are helpful for consumers to have for preparing home meals, and included some framing statistics emphasizing the weight management benefits of preparing meals versus eating out.

Target Market(s)

Women age 35-55

Industry/Entity Type

Health And Wellness

Font styles to use
Sans Serif

Colors
0292cd
9bcb3b

Requirements
Must have
• - FernQuill Logo
• - Graphics summarizing statistic (weight gain)
• - Graphics showing groupings of kitchen tools
Should not have
• body scale graphics
• before/after graphics

```html
<!DOCTYPE html>
<html lang="en">
<head>
<meta charset="UTF-8">
<title>Equip Your Kitchen for Healthy Home Meals | FernQuill</title>
<link rel="stylesheet" href="https://fonts.googleapis.com/css2?family=Black+Ops+One&family=Open+Sans:wght@400;600;700;800&family=Yellowtail&display=swap">
<style>
  :root {
    --blue: #0292cd;
    --green: #9bcb3b;
    --yellow: #f8b614;
    --orange: #f7941d;
    --dark: #363636;
    --cream: #fcfbe3;
    --header-cream: #f8f6d4;
    --fold: #b9b79f;
    --text: #333333;
  }
  * { box-sizing: border-box; margin: 0; padding: 0; }
  html, body { width: 1200px; height: 600px; overflow: hidden; background: var(--cream); }
  body { font-family: "Open Sans", Arial, sans-serif; color: var(--text); }
  .canvas { position: relative; width: 1200px; height: 600px; overflow: hidden; background: var(--cream); }

  /* Header */
  .header-bar { position: absolute; left: 0; top: 0; width: 1200px; height: 104px; background: var(--dark); }
  .title-panel { position: absolute; left: 0; top: 0; width: 688px; height: 76px; background: var(--header-cream); z-index: 2; }
  .brand { position: absolute; left: 22px; top: 24px; display: flex; align-items: center; gap: 6px; }
  .brand-dot { width: 22px; height: 22px; border-radius: 50%; background: var(--green); }
  .brand-name { font-family: "Open Sans", Arial, sans-serif; font-weight: 800; font-size: 19px; color: var(--green); white-space: nowrap; }
  .title-main { position: absolute; left: 162px; top: 4px; font-family: "Black Ops One", Impact, sans-serif; font-weight: 400; font-size: 29px; letter-spacing: 2px; color: var(--dark); white-space: nowrap; }
  .title-sub { position: absolute; left: 272px; top: 30px; font-family: "Yellowtail", cursive; font-size: 33px; line-height: 40px; color: var(--dark); white-space: nowrap; }
  .invite-panel { position: absolute; left: 616px; top: 36px; width: 584px; height: 58px; background: var(--header-cream); z-index: 1; }
  .fold { position: absolute; left: 616px; top: 76px; width: 0; height: 0; border-top: 18px solid var(--fold); border-right: 26px solid transparent; z-index: 3; }
  .invite-line { position: absolute; left: 0; width: 584px; text-align: center; font-size: 14.5px; color: var(--text); }
  .invite-line.first { top: 4px; padding-left: 60px; }
  .invite-line.second { top: 25px; padding-right: 140px; padding-left: 60px; }
  .invite-line strong { color: var(--blue); font-weight: 700; }
  .contact-button { position: absolute; left: 366px; top: 24px; width: 102px; height: 23px; background: var(--yellow); border: 2px solid #fbd57a; color: #fff; font-weight: 800; font-size: 12.5px; text-align: center; line-height: 19px; text-decoration: underline; letter-spacing: .5px; box-shadow: 2px 2px 0 #c98d00; }

  /* Statistics */
  .why-title { position: absolute; left: 32px; top: 164px; font-size: 14.5px; font-weight: 700; color: var(--blue); }
  .why-text { position: absolute; left: 32px; top: 186px; width: 256px; font-size: 9.6px; font-weight: 700; line-height: 14px; text-indent: 34px; color: var(--text); }
  .divider-v { position: absolute; left: 505px; top: 136px; width: 1px; height: 396px; background: #9a9a88; }
  .divider-h { position: absolute; left: 116px; top: 380px; width: 324px; height: 1px; background: #9a9a88; }
  .stat-label { position: absolute; font-weight: 700; white-space: nowrap; }
  .chart-caption { position: absolute; font-weight: 700; text-align: center; color: var(--text); white-space: nowrap; }

  .stats-art, .wheel-art { position: absolute; left: 0; top: 0; width: 1200px; height: 600px; }

  /* Tool callouts */
  .callout { position: absolute; background: var(--dark); color: #fff; border-radius: 4px; padding: 3px 4px; text-align: center; line-height: 1.15; }
  .callout-title { display: block; font-weight: 800; font-size: 7.5px; text-transform: uppercase; }
  .callout-text { display: block; font-weight: 700; font-size: 5.4px; }
  .callout.large .callout-title { font-size: 10px; }
  .callout.large .callout-text { font-size: 7px; }
  .callout.medium .callout-title { font-size: 8.5px; }
  .callout.medium .callout-text { font-size: 6.2px; }
</style>
</head>
<body>
<main class="canvas">

  <header>
    <div class="header-bar"></div>
    <div class="invite-panel">
      <p class="invite-line first"><strong>FernQuill</strong> can help you develop healthier eating habits.</p>
      <p class="invite-line second">We invite you to learn more.</p>
      <span class="contact-button">CONTACT US</span>
    </div>
    <div class="title-panel">
      <div class="brand"><span class="brand-dot"></span><span class="brand-name">FernQuill</span></div>
      <h1 class="title-main">EQUIP YOUR KITCHEN</h1>
      <p class="title-sub">for healthy Home Meals</p>
    </div>
    <div class="fold"></div>
  </header>

  <h2 class="why-title">Why Cook at Home?</h2>
  <p class="why-text">Those who eat out consume an average of 134 calories more per meal. Americans eat eat out an average of 4.5 times per week, so those extra calories can add up to substantial weight gain -- and give you a reason to prepare your own meals.</p>
  <div class="divider-v"></div>
  <div class="divider-h"></div>

  <svg class="stats-art" viewBox="0 0 1200 600" aria-hidden="true">
    <g transform="translate(372 232)">
      <circle r="49" fill="none" stroke="#0292cd" stroke-width="38" stroke-dasharray="251.5 400" transform="rotate(-24)"/>
      <circle r="52" fill="none" stroke="#9bcb3b" stroke-width="36" stroke-dasharray="49 400" transform="rotate(-82)"/>
      <text x="30" y="-39" font-family="Open Sans, sans-serif" font-weight="700" font-size="11" fill="#fff" text-anchor="middle">100</text>
      <text x="-30" y="34" font-family="Open Sans, sans-serif" font-weight="700" font-size="12" fill="#fff" text-anchor="middle">600</text>
    </g>
    <g fill="none" stroke-width="1.5">
      <polyline points="447,150 380,150 376,140" stroke="#9bcb3b"/>
      <polyline points="372,308 272,308 268,320" stroke="#0292cd"/>
    </g>
    <circle cx="447" cy="150" r="4" fill="#9bcb3b"/>
    <circle cx="372" cy="308" r="4" fill="#0292cd"/>

    <g transform="translate(224 456)">
      <circle r="49" fill="none" stroke="#0292cd" stroke-width="38" stroke-dasharray="152 400" transform="rotate(1)"/>
      <circle r="49" fill="none" stroke="#f8b614" stroke-width="38" stroke-dasharray="78 400" transform="rotate(183)"/>
      <circle r="49" fill="none" stroke="#9bcb3b" stroke-width="38" stroke-dasharray="71 400" transform="rotate(275)"/>
      <text x="-31" y="-26" font-family="Open Sans, sans-serif" font-weight="700" font-size="12" fill="#fff" text-anchor="middle">4.5 lbs</text>
      <text x="44" y="-18" font-family="Open Sans, sans-serif" font-weight="700" font-size="11" fill="#fff" text-anchor="middle">1.4 lbs</text>
      <text x="0" y="54" font-family="Open Sans, sans-serif" font-weight="700" font-size="12" fill="#fff" text-anchor="middle">8.96 lbs</text>
    </g>
    <g fill="none" stroke-width="1.5">
      <polyline points="150,424 84,424 76,412" stroke="#f8b614"/>
      <polyline points="298,412 365,412 372,426" stroke="#9bcb3b"/>
      <polyline points="224,534 88,534 80,546" stroke="#0292cd"/>
    </g>
    <circle cx="150" cy="424" r="4" fill="#f8b614"/>
    <circle cx="298" cy="412" r="4" fill="#9bcb3b"/>
    <circle cx="224" cy="534" r="4" fill="#0292cd"/>
  </svg>

  <span class="stat-label" style="left:300px;top:120px;font-size:11px;color:var(--green);">CALORIES PER MEAL</span>
  <span class="stat-label" style="left:204px;top:324px;font-size:11px;color:var(--blue);">CALORIES PER WEEK</span>
  <p class="chart-caption" style="left:246px;top:343px;font-size:12px;">Excess Calories from Restaurant Meals</p>
  <span class="stat-label" style="left:52px;top:384px;font-size:13px;font-weight:600;color:var(--yellow);">6 months</span>
  <span class="stat-label" style="left:366px;top:431px;font-size:13px;font-weight:600;color:var(--green);">2 months</span>
  <span class="stat-label" style="left:84px;top:553px;font-size:13px;font-weight:600;color:var(--blue);">1 year</span>
  <p class="chart-caption" style="left:296px;top:484px;width:180px;font-size:14.5px;font-weight:600;line-height:18px;">Pounds Gained<br>from Restaurant Meals</p>

  <svg class="wheel-art" viewBox="0 0 1200 600">
    <defs>
      <path id="segment" d="M -39.36 -212.4 A 216 216 0 0 1 39.36 -212.4 L 27.33 -147.5 A 150 150 0 0 0 -27.33 -147.5 Z"/>
    </defs>
    <g transform="translate(908 346)">
      <g transform="rotate(11.25)">
        <use href="#segment" fill="#363636"/>
        <text y="-188" font-family="Open Sans, sans-serif" font-weight="800" font-size="14" fill="#fff" text-anchor="middle">START</text>
        <text y="-172" font-family="Open Sans, sans-serif" font-weight="800" font-size="14" fill="#fff" text-anchor="middle">HERE</text>
      </g>
      <g transform="rotate(33.75)"><use href="#segment" fill="#f8b614"/><circle cy="-183" r="17" fill="#fff" opacity=".85" role="img" aria-label="Cutting board icon"/></g>
      <g transform="rotate(56.25)"><use href="#segment" fill="#f8b614"/><circle cy="-183" r="17" fill="#fff" opacity=".85" role="img" aria-label="Chef's knife icon"/></g>
      <g transform="rotate(78.75)"><use href="#segment" fill="#f8b614"/><circle cy="-183" r="17" fill="#fff" opacity=".85" role="img" aria-label="Food scale icon"/></g>
      <g transform="rotate(101.25)"><use href="#segment" fill="#9bcb3b"/><circle cy="-183" r="17" fill="#fff" opacity=".85" role="img" aria-label="Blender icon"/></g>
      <g transform="rotate(123.75)"><use href="#segment" fill="#9bcb3b"/><circle cy="-183" r="17" fill="#fff" opacity=".85" role="img" aria-label="Slow cooker icon"/></g>
      <g transform="rotate(146.25)"><use href="#segment" fill="#9bcb3b"/><circle cy="-183" r="17" fill="#fff" opacity=".85" role="img" aria-label="Pressure cooker icon"/></g>
      <g transform="rotate(168.75)"><use href="#segment" fill="#0292cd"/><circle cy="-183" r="17" fill="#fff" opacity=".85" role="img" aria-label="Baking sheet icon"/></g>
      <g transform="rotate(191.25)"><use href="#segment" fill="#0292cd"/><circle cy="-183" r="17" fill="#fff" opacity=".85" role="img" aria-label="Ceramic pan icon"/></g>
      <g transform="rotate(213.75)"><use href="#segment" fill="#0292cd"/><circle cy="-183" r="17" fill="#fff" opacity=".85" role="img" aria-label="Vegetable steamer icon"/></g>
      <g transform="rotate(236.25)"><use href="#segment" fill="#f7941d"/><circle cy="-183" r="17" fill="#fff" opacity=".85" role="img" aria-label="Small plates icon"/></g>
      <g transform="rotate(258.75)"><use href="#segment" fill="#f7941d"/><circle cy="-183" r="17" fill="#fff" opacity=".85" role="img" aria-label="Dinnerware icon"/></g>
      <g transform="rotate(281.25)"><use href="#segment" fill="#f7941d"/><circle cy="-183" r="17" fill="#fff" opacity=".85" role="img" aria-label="Cloth napkin icon"/></g>
      <g transform="rotate(303.75)"><use href="#segment" fill="#9bcb3b"/><circle cy="-183" r="17" fill="#fff" opacity=".85" role="img" aria-label="Mason jar icon"/></g>
      <g transform="rotate(326.25)"><use href="#segment" fill="#9bcb3b"/><circle cy="-183" r="17" fill="#fff" opacity=".85" role="img" aria-label="Resealable bag icon"/></g>
      <g transform="rotate(348.75)"><use href="#segment" fill="#9bcb3b"/><circle cy="-183" r="17" fill="#fff" opacity=".85" role="img" aria-label="Glass storage icon"/></g>
    </g>

    <g font-family="Open Sans, sans-serif" font-weight="800" text-anchor="middle">
      <text x="898" y="293" font-size="46" fill="#0292cd">MAKE</text>
      <text x="898" y="325" font-size="24" fill="#363636">HEALTHY EATING</text>
      <text x="898" y="370" font-size="44" fill="#f8b614">EASIER</text>
      <text x="898" y="400" font-size="18" fill="#363636">WITH THESE KITCHEN</text>
      <text x="898" y="442" font-size="42" fill="#9bcb3b">TOOLS</text>
    </g>

    <g font-family="Open Sans, sans-serif" font-weight="700">
      <circle cx="1066" cy="200" r="18" fill="#f8b614"/>
      <text x="1066" y="207" font-size="19" fill="#fff" text-anchor="middle">1</text>
      <text x="1092" y="208" font-size="20" fill="#f8b614">PREP:</text>

      <circle cx="1080" cy="488" r="18" fill="#9bcb3b"/>
      <text x="1080" y="495" font-size="19" fill="#fff" text-anchor="middle">2</text>
      <text x="1104" y="496" font-size="20" fill="#9bcb3b">TECH:</text>

      <circle cx="700" cy="568" r="18" fill="#0292cd"/>
      <text x="700" y="575" font-size="19" fill="#fff" text-anchor="middle">3</text>
      <text x="724" y="576" font-size="20" fill="#0292cd">COOK:</text>

      <circle cx="570" cy="352" r="18" fill="#f7941d"/>
      <text x="570" y="359" font-size="19" fill="#fff" text-anchor="middle">4</text>
      <text x="594" y="360" font-size="19" fill="#f7941d">SERVE:</text>

      <circle cx="594" cy="182" r="18" fill="#9bcb3b"/>
      <text x="594" y="189" font-size="19" fill="#fff" text-anchor="middle">5</text>
      <text x="618" y="190" font-size="18" fill="#9bcb3b">STORE:</text>
    </g>
  </svg>

  <div class="callout large" style="left:776px;top:130px;width:106px;"><span class="callout-title">Glass Storage</span><span class="callout-text">Keep your healthy leftovers so nothing goes to waste.</span></div>
  <div class="callout" style="left:692px;top:162px;width:84px;"><span class="callout-title">Resealable Bag</span><span class="callout-text">Prepare double batches to make the most of your time.</span></div>
  <div class="callout" style="left:652px;top:208px;width:84px;"><span class="callout-title">Mason Jar</span><span class="callout-text">Perfect for premade salads that you can bring to work.</span></div>
  <div class="callout" style="left:964px;top:172px;width:70px;"><span class="callout-title">Cutting Board</span><span class="callout-text">Essential for prepping meat and vegetables.</span></div>
  <div class="callout" style="left:1032px;top:232px;width:66px;"><span class="callout-title">Chef's Knife</span><span class="callout-text">Go for quality to make chopping, dicing and slicing faster and easier.</span></div>
  <div class="callout" style="left:1056px;top:298px;width:66px;"><span class="callout-title">Food Scale</span><span class="callout-text">Get the precision you need for perfect recipes and portion control.</span></div>
  <div class="callout" style="left:1054px;top:348px;width:66px;"><span class="callout-title">High-Powered Blender</span><span class="callout-text">Make highly nutritious, healthy drinks from fruits and veggies.</span></div>
  <div class="callout" style="left:1042px;top:428px;width:68px;"><span class="callout-title">Slow Cooker</span><span class="callout-text">Cook delicious meals while you are at work.</span></div>
  <div class="callout" style="left:990px;top:496px;width:66px;"><span class="callout-title">Pressure Cooker</span><span class="callout-text">Create single pot meals in 20 minutes or less.</span></div>
  <div class="callout" style="left:894px;top:536px;width:86px;"><span class="callout-title">Baking Sheet</span><span class="callout-text">Ideal for roasting vegetables in the oven or baking chicken and fish dishes</span></div>
  <div class="callout" style="left:806px;top:542px;width:64px;"><span class="callout-title">Ceramic Pan</span><span class="callout-text">Nonstick cooking surface allows you to cook without oil</span></div>
  <div class="callout medium" style="left:708px;top:510px;width:82px;"><span class="callout-title">Vegetable Steamer</span><span class="callout-text">Preserve nutrients and natural, fresh taste.</span></div>
  <div class="callout medium" style="left:596px;top:454px;width:130px;"><span class="callout-title">Small Plates</span><span class="callout-text">Use salad plates and smaller dishware to manage perception of food volume</span></div>
  <div class="callout medium" style="left:588px;top:382px;width:108px;"><span class="callout-title">Dinnerware</span><span class="callout-text">Pre-plate meals rather than serving family style to control portions</span></div>
  <div class="callout medium" style="left:616px;top:288px;width:80px;"><span class="callout-title">Cloth Napkin</span><span class="callout-text">To reduce waste and dress up your table</span></div>

</main>
</body>
</html>
```